Merrivale construction website for a high end luxury custom home builder

I need a website designed for a high end luxury custom home builder. I would like the website to host a number activities. A blog/vlog on the page where I can post about the projects being built how to's what to look out for during the build, A designated testimonial page but also having testimonials posted on the other pages like the gallery linked to the photos of the completed projects. a gallery page, an about us page, services page that demonstrate what we do and what we are capable of, and hopefully when I start winning awards, and awards page.
Home page
about us page
services page
gallery
testimonial
awards page but I my need to add that later.
I already have the domain name for the website. www.merrivaleconstruction.com.au
I recently completed a sketch hive page for my logo and will post the logo documents below.

Target Market(s)

I'd like to target professions with cash enough to build a house. I would like peolpe to understand that they are buy a price when they are getting quote to build there house. It seems like people just look for the cheapest price and end up with an inferior product. Where as people need to understand that a builder with the high price ( not astronomically higher 15-20% higher) are the ones with correct systems in place, a bide by correct OHS and use proper and correct product. If that can be conveyed through the website somehow, without saying it directly, it would be awesome.

Font styles to use
Sans Serif

Requirements
Must have
• I would like the testimonials to have a designated page (mentioned in the brief) but I would like the testimonials to be linked to the gallery page and when the picture are open of completed job the relevant testimonials would pop up near the pictures.

Nice to have
• I would like peolpe to understand that they are buy a price when they are getting quote to build there house. It seems like people just look for the cheapest price and end up with an inferior product. Where as people need to understand that a builder with the high price ( not astronomically higher 15-20% higher) are the ones with correct systems in place, a bide by correct OHS and use proper and correct product. If that can be conveyed through the website somehow, without saying it directly, it would be awesome.

```html
<!DOCTYPE html>
<html lang="en">
<head>
<meta charset="utf-8">
<title>Merrivale Construction</title>
<link rel="stylesheet" href="https://fonts.googleapis.com/css2?family=Oswald:wght@300;400&family=Roboto:wght@300;400;500&display=swap">
<style>
:root{
  --blue:#0a7fe0;
  --ink:#1d1d1d;
  --body:#555a60;
  --muted:#7a7f85;
  --line:#e4e7ea;
  --pale:#eef4fb;
  --footer:#141c27;
  --footer-text:#a9b0b9;
  --white:#ffffff;
}
*{box-sizing:border-box;margin:0;padding:0}
html,body{width:1200px;height:4377px;overflow:hidden;background:var(--white)}
body{font-family:'Roboto',sans-serif;color:var(--body);position:relative}
.page{position:relative;width:1200px;height:4377px;overflow:hidden}
.abs{position:absolute}
.heading{font-family:'Oswald',sans-serif;font-weight:400;color:var(--ink);text-transform:uppercase;letter-spacing:.3px}
.rule{display:block;width:38px;height:3px;background:var(--blue);margin-top:8px}
.center{text-align:center}
.center .rule{margin:8px auto 0}
.btn{display:inline-flex;align-items:center;justify-content:center;border-radius:18px;font-family:'Oswald',sans-serif;font-size:14px;text-transform:uppercase;letter-spacing:.3px}
.btn-solid{background:var(--blue);color:var(--white)}
.btn-ghost{border:1.5px solid var(--blue);color:var(--blue);background:var(--white)}

/* header */
.site-header{left:0;top:0;width:1200px;height:88px;background:var(--white);z-index:5}
.brand{display:flex;align-items:center;gap:8px;font-family:'Oswald',sans-serif;font-weight:400;font-size:22px;letter-spacing:1px;color:var(--blue)}
.brand-mark{width:14px;height:14px;background:var(--blue)}
.site-header .brand{position:absolute;left:88px;top:30px}
.nav{position:absolute;left:500px;top:36px;display:flex;gap:0;font-family:'Oswald',sans-serif;font-weight:300;font-size:14px;color:#444}
.nav a{text-decoration:none;color:inherit;position:absolute;top:8px;white-space:nowrap}
.nav a.active{color:var(--ink)}
.nav a.active::after{content:"";position:absolute;left:0;right:0;bottom:-6px;height:2px;background:var(--blue)}
.nav .btn{position:absolute;top:0;width:114px;height:36px;font-size:14px}

/* hero */
.hero{left:0;top:88px;width:1200px;height:610px;background:linear-gradient(180deg,#7f98ad 0%,#9aa9b6 30%,#8a8f95 55%,#4a4e53 80%,#2e3034 100%)}
.hero-title{left:0;top:278px;width:1200px;text-align:center;font-family:'Oswald',sans-serif;font-weight:300;font-size:58px;color:var(--white);letter-spacing:.5px}
.hero-sub{left:250px;top:360px;width:700px;text-align:center;font-size:15px;line-height:19px;color:var(--white)}
.hero-btn{left:528px;top:430px;width:144px;height:36px;border:1.5px solid var(--white);border-radius:18px;color:var(--white);font-size:14px;display:flex;align-items:center;justify-content:center;gap:10px;letter-spacing:.5px}
.dots{display:flex;gap:8px}
.dots i{width:8px;height:8px;border-radius:50%;border:1.3px solid var(--blue);display:block}
.dots i.on{background:var(--blue)}
.hero .dots i{border-color:var(--white)}
.hero .dots i.on{background:var(--white)}

/* about */
.about-text{left:175px;top:788px;width:430px}
.about-text .heading{font-size:26px}
.about-lead{margin-top:22px;font-family:'Oswald',sans-serif;font-weight:300;font-size:13.5px;line-height:18px;color:#555;text-transform:uppercase}
.about-body{margin-top:20px;font-size:13.5px;line-height:18px;color:#555}
.about-photo{left:679px;top:725px;width:426px;height:426px;border-radius:50%;background:radial-gradient(circle at 40% 45%,#f2efe9 0%,#e2ddd4 50%,#b9a98f 85%,#8f7a5e 100%)}

/* services */
.services-bg{left:0;top:1190px;width:1200px;height:670px;background:linear-gradient(90deg,#5c6168 0%,#7b8087 40%,#8e9297 70%,#a59c7d 100%)}
.services-text{left:175px;top:1308px;width:380px;color:var(--white)}
.services-text .heading{color:var(--white);font-size:26px}
.services-text p{margin-top:28px;font-family:'Oswald',sans-serif;font-weight:300;font-size:14px;line-height:18px}
.service-card{width:237px;height:268px;background:var(--white);box-shadow:0 4px 14px rgba(0,0,0,.12);text-align:center;padding-top:32px}
.service-card svg{display:block;margin:0 auto}
.service-card h3{margin-top:18px;font-family:'Oswald',sans-serif;font-weight:400;font-size:16px;line-height:20px;color:var(--ink);text-transform:uppercase}
.service-card hr{border:0;height:1px;background:var(--line);width:120px;margin:10px auto 14px}
.service-card p{padding:0 22px;font-size:13.5px;line-height:18px;color:#666}

/* projects */
.projects-head{left:0;top:1940px;width:1200px}
.projects-head .heading{font-size:26px}
.sub{margin-top:22px;font-family:'Oswald',sans-serif;font-weight:300;font-size:14px;line-height:18px;color:#555;text-transform:uppercase}
.tabs{left:0;top:2080px;width:1200px;display:flex;justify-content:center;gap:26px;font-family:'Oswald',sans-serif;font-weight:400;font-size:14px;color:var(--ink)}
.tabs .on{color:var(--blue)}
.project{width:270px;height:420px;background:var(--white);box-shadow:0 3px 12px rgba(0,0,0,.09)}
.project .shot{height:217px}
.project h3{margin:16px 0 0 27px;font-family:'Oswald',sans-serif;font-weight:400;font-size:16px;color:var(--ink)}
.project ul{list-style:none;margin:12px 0 0 27px;font-size:12.5px;color:var(--muted)}
.project li{display:flex;align-items:center;gap:10px;height:34px}
.project .actions{margin:6px 0 0 25px;display:flex;gap:14px}
.project .btn{height:26px;width:86px;font-size:12px;border-radius:14px}

/* clients */
.clients-bg{left:0;top:2640px;width:1200px;height:710px;background:var(--pale)}
.clients-head{left:0;top:2710px;width:1200px}
.clients-head .heading{font-size:26px}
.testimonial{left:155px;top:2790px;width:890px;height:302px;background:var(--white)}
.testimonial .shot{position:absolute;left:0;top:0;width:445px;height:302px;background:linear-gradient(180deg,#a7c2dc 0%,#c8d6e0 35%,#7f6f5c 60%,#3e5a2c 85%,#2f4a22 100%)}
.avatar{left:555px;top:2889px;width:92px;height:92px;border-radius:50%;border:4px solid var(--white);background:linear-gradient(160deg,#c9c6c2,#6d6660);box-shadow:0 2px 8px rgba(0,0,0,.15)}
.quote-name{left:668px;top:2878px;font-family:'Oswald',sans-serif;font-weight:400;font-size:16px;color:var(--blue);text-transform:uppercase}
.quote-mark{left:666px;top:2850px;font-family:'Oswald',sans-serif;font-size:70px;line-height:1;color:#dbe8f5}
.stars{left:906px;top:2878px;display:flex;gap:2px}
.quote-text{left:668px;top:2915px;width:345px;font-size:13.5px;line-height:18.5px;color:#666;text-align:justify}
.thumb{top:3215px;width:122px;height:68px;border:1px solid #c9d6e3}
.thumb.big{top:3158px;width:186px;height:124px;border:2px solid var(--blue)}
.arrow{top:3222px;width:56px;height:56px;border-radius:50%;border:2px solid #9aa3ad;display:flex;align-items:center;justify-content:center}

/* blog */
.blog-head{left:0;top:3390px;width:1200px}
.blog-head .heading{font-size:26px}
.blog-head .sub{text-transform:none;font-size:14px;margin-top:22px}
.post{width:220px}
.post .shot{height:188px}
.post h3{margin-top:30px;font-family:'Oswald',sans-serif;font-weight:400;font-size:13.5px;color:var(--ink)}
.post p{margin-top:12px;font-size:12.5px;line-height:16.5px;color:#777}
.post hr{border:0;height:1px;background:var(--line);margin-top:10px}
.post .meta{margin-top:10px;display:flex;justify-content:space-between;font-family:'Oswald',sans-serif;font-weight:300;font-size:12.5px;color:var(--blue)}
.overlay-link{left:0;right:0;top:104px;text-align:center;color:var(--white);font-family:'Oswald',sans-serif;font-size:13px}

/* footer */
.site-footer{left:0;top:3918px;width:1200px;height:459px;background:var(--footer);color:var(--footer-text)}
.site-footer .brand{position:absolute;left:88px;top:100px;color:var(--white)}
.site-footer .brand-mark{background:var(--white)}
.contact-lines{left:88px;top:184px;font-size:15px;line-height:22px}
.socials{left:88px;top:256px;display:flex;gap:18px}
.socials i{width:14px;height:14px;border-radius:50%;background:var(--footer-text);display:block}
.col h4{font-weight:400;font-size:15px;color:var(--blue)}
.col ul{list-style:none;margin-top:26px;font-size:15px}
.col li{height:36px}
.news h4{font-weight:400;font-size:15px;color:var(--white)}
.news .field{margin-top:24px;width:235px;height:36px;border-radius:18px;background:var(--white);color:#888;font-size:12.5px;padding:11px 14px}
.news .btn{margin-top:24px;width:104px;height:32px;font-family:'Roboto',sans-serif;font-size:13.5px;text-transform:none}
.footer-rule{left:88px;top:382px;width:1024px;height:1px;background:#2c3542}
.copyright{left:88px;top:412px;font-size:13px;color:var(--footer-text)}
.copyright span{color:var(--blue)}
</style>
</head>
<body>
<div class="page">

  <!-- header -->
  <header class="abs site-header">
    <div class="brand"><span class="brand-mark"></span>MERRIVALE</div>
    <nav class="nav">
      <a class="active" style="left:0">HOME</a>
      <a style="left:86px">ABOUT</a>
      <a style="left:182px">SERVICE</a>
      <a style="left:290px">GALLERY</a>
      <a style="left:400px">AWARDS</a>
      <span class="btn btn-solid" style="left:498px">CONTACT</span>
    </nav>
  </header>

  <!-- hero -->
  <section class="abs hero" role="img" aria-label="Modern white luxury house with balconies and glass railings against a blue sky">
    <div class="abs dots" style="left:576px;top:510px"><i class="on"></i><i></i><i></i></div>
  </section>
  <h1 class="abs hero-title">BUILD YOUR DREAM HOUSE</h1>
  <p class="abs hero-sub">The first step in selling your property is to get a valuation from local experts. They will inspect your home and take into account its unique features</p>
  <div class="abs hero-btn">EXPLORE
    <svg width="22" height="12" viewBox="0 0 22 12" fill="none" stroke="#fff" stroke-width="1.5"><path d="M1 6h19M15 1l5 5-5 5"/></svg>
  </div>
  <svg class="abs" style="left:0;top:600px" width="1200" height="110" viewBox="0 0 1200 110">
    <path d="M0 45 C 250 0, 500 70, 760 50 S 1100 30, 1200 60 L1200 110 L0 110 Z" fill="#fff"/>
    <path d="M0 48 C 250 8, 500 72, 760 54 S 1100 36, 1200 62" fill="none" stroke="#2b3a4a" stroke-width="3"/>
  </svg>

  <!-- about -->
  <div class="abs about-text">
    <h2 class="heading">Few words about us<span class="rule"></span></h2>
    <p class="about-lead">Our construction company has been founded 10 years ago, at the very peak of the building frenzy in the US...</p>
    <p class="about-body">Since then we've built hundreds of commercial, government and private buildings and facilities. It may not sound like a lot, but if you estimate the manpower, working hours, materials, planning and correlating that were all involved in completing each separate project, then our productivity is immense!</p>
    <span class="btn btn-solid" style="margin-top:40px;width:114px;height:34px">READ MORE</span>
  </div>
  <div class="abs about-photo" role="img" aria-label="Bright open-plan living and dining room with wooden floor"></div>
  <svg class="abs" style="left:655px;top:700px" width="470" height="470" viewBox="0 0 470 470" fill="none" stroke="#1f7fd6" stroke-width="1.2">
    <path d="M244 8 L457 243 L222 460 L8 226 Z"/>
    <path d="M244 8 L416 193"/>
  </svg>

  <!-- services -->
  <div class="abs services-bg" role="img" aria-label="Modern kitchen interior with white island bench and large windows"></div>
  <svg class="abs" style="left:0;top:1180px" width="1200" height="60" viewBox="0 0 1200 60">
    <path d="M0 0 H1200 V24 C 950 6, 700 2, 430 20 C 250 32, 120 30, 0 20 Z" fill="#fff"/>
  </svg>
  <svg class="abs" style="left:0;top:1800px" width="1200" height="70" viewBox="0 0 1200 70">
    <path d="M0 45 C 250 62, 600 62, 850 40 C 1000 26, 1120 14, 1200 8 V70 H0 Z" fill="#fff"/>
  </svg>
  <div class="abs services-text">
    <h2 class="heading">High - quality services<span class="rule" style="background:#fff"></span></h2>
    <p>We aim to make clients happy by selling the best products at the best prices, in a friendly, fun atmosphere. Our rating has remained at 100% with excellent and positive feedbacks. We are constantly adding new products.</p>
    <span class="btn btn-solid" style="margin-top:26px;width:114px;height:32px">VIEW MORE</span>
  </div>

  <article class="abs service-card" style="left:598px;top:1310px">
    <svg width="64" height="58" viewBox="0 0 64 58" fill="none" stroke="#222" stroke-width="1.6"><path d="M20 22 L34 10 L48 22 V34 H20 Z"/><path d="M30 34 V26 H38 V34"/><path d="M6 40 H18 L30 44 H42 C46 44 46 49 42 49 H30 M42 47 L56 40 C60 38 62 43 58 45 L40 54 H6"/></svg>
    <h3>Construction<br>services</h3><hr>
    <p>We provide high-quality construction services to a wide variety of clients.</p>
  </article>
  <article class="abs service-card" style="left:876px;top:1310px">
    <svg width="64" height="58" viewBox="0 0 64 58" fill="none" stroke="#1f6fc4" stroke-width="1.6"><rect x="8" y="10" width="48" height="38"/><path d="M8 20 H56 M22 10 V48 M40 10 V48 M22 34 H56"/><path d="M28 14 L36 42"/></svg>
    <h3>Construction<br>management</h3><hr>
    <p>We develop and implement better interior design concepts for you.</p>
  </article>
  <article class="abs service-card" style="left:598px;top:1620px">
    <svg width="64" height="58" viewBox="0 0 64 58" fill="none" stroke="#222" stroke-width="1.6"><rect x="6" y="22" width="52" height="22"/><path d="M10 44 V52 M54 44 V52 M32 22 V44"/><rect x="12" y="8" width="14" height="14"/><path d="M40 22 V12 H52 V22"/></svg>
    <h3>Interior design</h3><hr>
    <p>We develop and implement better interior design concepts for you.</p>
  </article>
  <article class="abs service-card" style="left:876px;top:1620px">
    <svg width="64" height="58" viewBox="0 0 64 58" fill="none" stroke="#222" stroke-width="1.6"><path d="M14 6 C8 12 10 18 16 18 L46 48 L52 42 L22 12 C22 6 16 4 14 6 Z"/><path d="M50 8 L36 22 M44 6 L54 16 L40 30"/><path d="M26 32 L12 46 L16 50 L30 36"/></svg>
    <h3>Consultations</h3><hr>
    <p>Our specialists are ready to consult you on any interior design related topic.</p>
  </article>

  <!-- projects -->
  <div class="abs projects-head center">
    <h2 class="heading">Our projects<span class="rule"></span></h2>
    <p class="sub">Our construction company has been founded 10 years ago, at<br>the very peak of the building frenzy in the US...</p>
  </div>
  <div class="abs tabs"><span class="on">HOME</span><span>APARTMENTS</span><span>PLOTS</span></div>

  <article class="abs project" style="left:155px;top:2138px">
    <div class="shot" role="img" aria-label="Covered outdoor lounge beside a garden with tall trees" style="background:linear-gradient(180deg,#6f8a5a 0%,#c8bfae 40%,#8f8a84 70%,#5e6166 100%)"></div>
    <h3>The Luxury Royale Phase</h3>
    <ul>
      <li><svg width="12" height="14" viewBox="0 0 12 14" fill="none" stroke="#0a7fe0" stroke-width="1.3"><path d="M6 13 C2 8 1 6 1 5 A5 5 0 0 1 11 5 C11 6 10 8 6 13 Z"/><circle cx="6" cy="5" r="1.8"/></svg>Place of the Home</li>
      <li><svg width="14" height="12" viewBox="0 0 14 12" fill="none" stroke="#0a7fe0" stroke-width="1.3"><rect x="1" y="2" width="12" height="8"/><path d="M1 6 H13"/></svg>2, 3 &amp; 4 BHK Rooms</li>
      <li><svg width="13" height="13" viewBox="0 0 13 13" fill="none" stroke="#0a7fe0" stroke-width="1.3"><circle cx="6.5" cy="6.5" r="5.5"/><path d="M6.5 3 V10"/></svg>From $699 Onwards</li>
    </ul>
    <div class="actions"><span class="btn btn-ghost">GET QUOTE</span></div>
  </article>
  <article class="abs project" style="left:465px;top:2138px">
    <div class="shot" role="img" aria-label="Villa courtyard with a turquoise swimming pool" style="background:linear-gradient(180deg,#6fa8d6 0%,#d8c7a5 40%,#3fb0c4 70%,#2f8da3 100%)"></div>
    <h3>The Luxury Royale Phase</h3>
    <ul>
      <li><svg width="12" height="14" viewBox="0 0 12 14" fill="none" stroke="#0a7fe0" stroke-width="1.3"><path d="M6 13 C2 8 1 6 1 5 A5 5 0 0 1 11 5 C11 6 10 8 6 13 Z"/><circle cx="6" cy="5" r="1.8"/></svg>Place of the Home</li>
      <li><svg width="14" height="12" viewBox="0 0 14 12" fill="none" stroke="#0a7fe0" stroke-width="1.3"><rect x="1" y="2" width="12" height="8"/><path d="M1 6 H13"/></svg>2, 3 &amp; 4 BHK Rooms</li>
      <li><svg width="13" height="13" viewBox="0 0 13 13" fill="none" stroke="#0a7fe0" stroke-width="1.3"><circle cx="6.5" cy="6.5" r="5.5"/><path d="M6.5 3 V10"/></svg>From $699 Onwards</li>
    </ul>
    <div class="actions"><span class="btn btn-ghost">GET QUOTE</span><span class="btn btn-solid">VIEW</span></div>
  </article>
  <article class="abs project" style="left:775px;top:2138px">
    <div class="shot" role="img" aria-label="Contemporary glass-fronted house with a poolside deck" style="background:linear-gradient(180deg,#d9dcdf 0%,#8c9397 40%,#4b5257 70%,#3a6a78 100%)"></div>
    <h3>The Luxury Royale Phase</h3>
    <ul>
      <li><svg width="12" height="14" viewBox="0 0 12 14" fill="none" stroke="#0a7fe0" stroke-width="1.3"><path d="M6 13 C2 8 1 6 1 5 A5 5 0 0 1 11 5 C11 6 10 8 6 13 Z"/><circle cx="6" cy="5" r="1.8"/></svg>Place of the Home</li>
      <li><svg width="14" height="12" viewBox="0 0 14 12" fill="none" stroke="#0a7fe0" stroke-width="1.3"><rect x="1" y="2" width="12" height="8"/><path d="M1 6 H13"/></svg>2, 3 &amp; 4 BHK Rooms</li>
      <li><svg width="13" height="13" viewBox="0 0 13 13" fill="none" stroke="#0a7fe0" stroke-width="1.3"><circle cx="6.5" cy="6.5" r="5.5"/><path d="M6.5 3 V10"/></svg>From $699 Onwards</li>
    </ul>
    <div class="actions"><span class="btn btn-ghost">GET QUOTE</span></div>
  </article>
  <div class="abs dots" style="left:578px;top:2594px"><i class="on"></i><i></i><i></i></div>

  <!-- clients -->
  <div class="abs clients-bg"></div>
  <svg class="abs" style="left:0;top:2620px" width="1200" height="60" viewBox="0 0 1200 60">
    <path d="M0 40 C 300 8, 600 48, 900 24 C 1050 12, 1150 14, 1200 20 V60 H0 Z" fill="#e3eef9"/>
    <path d="M0 52 C 300 26, 650 56, 950 36 C 1080 28, 1160 30, 1200 34 V60 H0 Z" fill="#eef4fb"/>
  </svg>
  <svg class="abs" style="left:0;top:3310px" width="1200" height="80" viewBox="0 0 1200 80">
    <path d="M0 40 C 300 70, 700 10, 1200 36 V80 H0 Z" fill="#fff"/>
  </svg>
  <div class="abs clients-head center"><h2 class="heading">Our clients say<span class="rule"></span></h2></div>
  <div class="abs testimonial"><div class="shot" role="img" aria-label="Large Tudor-style house among green trees"></div></div>
  <div class="abs avatar" role="img" aria-label="Client portrait"></div>
  <div class="abs quote-mark">“</div>
  <div class="abs quote-name">Adrian Holt</div>
  <div class="abs stars">
    <svg width="106" height="20" viewBox="0 0 106 20" fill="#f5b301"><path id="st" d="M10 1 L12.6 7 L19 7.5 L14 11.7 L15.6 18 L10 14.6 L4.4 18 L6 11.7 L1 7.5 L7.4 7 Z"/><use href="#st" x="21"/><use href="#st" x="42"/><use href="#st" x="63"/><use href="#st" x="84"/></svg>
  </div>
  <p class="abs quote-text">It`s no secret testimonials are the driving force behind purchasing decisions. They are such a great way to create immediate trust with prospective clients. Testimonials are one of the most important factors for users when deciding on if they want to use your product or service.</p>

  <div class="abs arrow" style="left:88px"><svg width="16" height="20" viewBox="0 0 16 20" fill="none" stroke="#9aa3ad" stroke-width="2"><path d="M12 2 L4 10 L12 18"/></svg></div>
  <div class="abs arrow" style="left:1027px"><svg width="16" height="20" viewBox="0 0 16 20" fill="none" stroke="#9aa3ad" stroke-width="2"><path d="M4 2 L12 10 L4 18"/></svg></div>
  <div class="abs thumb" style="left:206px;background:linear-gradient(180deg,#cfd6dc,#5d5a52)" role="img" aria-label="House exterior thumbnail"></div>
  <div class="abs thumb" style="left:352px;background:linear-gradient(180deg,#6f93bf,#4a4d55)" role="img" aria-label="House at dusk thumbnail"></div>
  <div class="abs thumb big" style="left:500px;background:linear-gradient(180deg,#a7c2dc,#7f6f5c 55%,#3e5a2c)" role="img" aria-label="Tudor-style house thumbnail"></div>
  <div class="abs thumb" style="left:716px;background:linear-gradient(180deg,#a4b55a,#4f5a2e)" role="img" aria-label="Garden house thumbnail"></div>
  <div class="abs thumb" style="left:862px;background:linear-gradient(180deg,#7ea05a,#b9b6ae)" role="img" aria-label="Cottage driveway thumbnail"></div>
  <div class="abs dots" style="left:582px;top:3313px"><i class="on"></i><i></i><i></i></div>

  <!-- blog -->
  <div class="abs blog-head center">
    <h2 class="heading">Latest blog<span class="rule"></span></h2>
    <p class="sub">On the other hand, we denounce with righteous indignation and dislike men who are so beguiled and<br>demoralized by the charms of pleasure of the moment, so blinded by desire</p>
  </div>
  <article class="abs post" style="left:242px;top:3513px">
    <div class="shot" role="img" aria-label="White kitchen with wooden floor" style="background:linear-gradient(180deg,#f0efed,#d8d2c8 60%,#a58462)"></div>
    <h3>Construction Company Services</h3>
    <p>Our Construction Company is a superior provider of housing, educational and support services</p>
    <hr>
  </article>
  <article class="abs post" style="left:490px;top:3513px">
    <div class="shot" role="img" aria-label="Modern house facade behind a dark overlay" style="background:linear-gradient(180deg,#5e6166,#3f4246)"></div>
    <div class="abs overlay-link">READ MORE</div>
    <h3>Construction Company Services</h3>
    <p>Our Construction Company is a superior provider of housing, educational and support services for indi</p>
    <hr>
    <div class="meta"><span>May 11, 2020</span><span>▭ 13</span></div>
  </article>
  <article class="abs post" style="left:738px;top:3513px">
    <div class="shot" role="img" aria-label="Suburban house lit at twilight" style="background:linear-gradient(180deg,#5f86c4 0%,#8d7b5c 55%,#5a6548 100%)"></div>
    <h3>Construction Company Services</h3>
    <p>Our Construction Company is a superior provider of housing, educational and support services for individuals</p>
    <hr>
  </article>

  <!-- footer -->
  <footer class="abs site-footer">
    <div class="brand"><span class="brand-mark"></span>MERRIVALE</div>
    <div class="abs contact-lines">Phone: 800 555 0142<br>Email: info@merrivale.com</div>
    <div class="abs socials" aria-label="Social links"><i></i><i></i><i></i><i></i></div>
    <div class="abs col" style="left:472px;top:104px">
      <h4>Menus</h4>
      <ul><li>Home</li><li>About Us</li><li>Services</li><li>Blog</li><li>Contact Us</li></ul>
    </div>
    <div class="abs col" style="left:664px;top:104px">
      <h4>Useful Links</h4>
      <ul><li>Quotes</li><li>Supports</li><li>Terms &amp; condition</li><li>Privacy Policy</li></ul>
    </div>
    <div class="abs news" style="left:877px;top:104px">
      <h4>Newsletter</h4>
      <div class="field">Enter your E- mail</div>
      <span class="btn btn-solid">Subscribe</span>
    </div>
    <div class="abs footer-rule"></div>
    <p class="abs copyright">© 2020 <span>Merrivale construction</span>. All rights reserved.</p>
  </footer>
</div>
</body>
</html>
```